Fireworks company

COLORFUL design, incorporating logo (attached).
Information to be included:
PO BOX 4827
Highton Victoria 3381
Ph 03 5461 2839
Fax 03 5487 9016
Email sales@halbrenncelebrations.com.au
Web www.halbrenncelebrations.com.au

Check out our website for more inspiration? :-)

```html
<!DOCTYPE html>
<html lang="en">
<head>
<meta charset="utf-8">
<title>Halbrenn Celebrations Letterhead</title>
<link href="https://fonts.googleapis.com/css2?family=Encode+Sans+Condensed:wght@400;500;700&display=swap" rel="stylesheet">
<style>
  :root {
    --paper-top: #ffffff;
    --paper-bottom: #f4f3ea;
    --brand-orange: #f98600;
    --brand-red: #ec4a12;
    --ink: #3b2a1c;
    --rule: #e05a1a;
  }
  html, body {
    margin: 0;
    padding: 0;
    overflow: hidden;
    background: #ffffff;
  }
  .letterhead {
    position: relative;
    width: 848px;
    height: 1200px;
    overflow: hidden;
    background: linear-gradient(to bottom, var(--paper-top) 0%, var(--paper-bottom) 30%, var(--paper-bottom) 100%);
    font-family: "Encode Sans Condensed", "Arial Narrow", sans-serif;
    color: var(--ink);
  }
  .brand {
    position: absolute;
    left: 32px;
    top: 40px;
    display: flex;
    align-items: center;
    gap: 12px;
  }
  .brand-dot {
    width: 22px;
    height: 22px;
    border-radius: 50%;
    background: var(--brand-orange);
  }
  .brand-name {
    font-weight: 700;
    font-size: 29px;
    line-height: 1.05;
    color: var(--brand-red);
    text-transform: uppercase;
    letter-spacing: 0.5px;
  }
  .contact-left {
    position: absolute;
    right: 262px;
    top: 48px;
    text-align: right;
    font-size: 14.5px;
    line-height: 19.5px;
  }
  .contact-rule {
    position: absolute;
    left: 598px;
    top: 43px;
    width: 2px;
    height: 67px;
    background: var(--rule);
  }
  .contact-right {
    position: absolute;
    left: 613px;
    top: 56px;
    font-size: 13.5px;
    line-height: 19.5px;
    white-space: nowrap;
  }
  .footer-band {
    position: absolute;
    left: 0;
    bottom: 0;
    width: 848px;
    height: 200px;
  }
  .footer-email {
    position: absolute;
    left: 0;
    width: 848px;
    top: 1155px;
    text-align: center;
    font-size: 19px;
    font-weight: 500;
    color: var(--ink);
  }
</style>
</head>
<body>
<main class="letterhead">
  <header>
    <div class="brand">
      <span class="brand-dot"></span>
      <span class="brand-name">Halbrenn<br>Celebrations</span>
    </div>
    <div class="contact-left">
      <div>PO BOX : 4827</div>
      <div>Ph : 03 5461 2839</div>
      <div>Fax : 03 5487 9016</div>
    </div>
    <div class="contact-rule"></div>
    <div class="contact-right">
      <div>Address : Tarrenby Norvale 3381</div>
      <div>Web : www.halbrenncelebrations.com.au</div>
    </div>
  </header>

  <svg class="footer-band" viewBox="0 1000 848 200" preserveAspectRatio="none" aria-hidden="true">
    <path d="M0 1131 Q 520 1140 848 1043 L848 1200 L0 1200 Z" fill="var(--brand-orange)"/>
    <path d="M646 1170 Q 760 1148 848 1128 L848 1154 Q 750 1162 646 1170 Z" fill="var(--paper-bottom)"/>
  </svg>
  <div class="footer-email">Email sales@halbrenncelebrations.com.au</div>
</main>
</body>
</html>
```